I need a better looking dashboard for my web application

I have a very table heavy web page that I would like to add a design touch to it. I have the logo and primary colors picked out, I just need some help in adding visual appeal the page. I would also like to add a couple of button to the page as shortcuts. Every spot that has a + sign could have a button added. I would also like to add another graph (the data will be in the uploaded files. Please feel free to ask any questions :-)

```html
<!DOCTYPE html>
<html lang="en">
<head>
<meta charset="utf-8">
<title>ShiftCover Dashboard Screens</title>
<link href="https://fonts.googleapis.com/css2?family=Nunito+Sans:wght@400;600;700&display=swap" rel="stylesheet">
<style>
:root{
  --purple:#6a50a7;
  --purple-btn:#6246ad;
  --cyan:#1fa7d9;
  --ink:#2b2b3a;
  --muted:#5b5b6b;
  --line:#e7e7ef;
  --blue:#18a9f5;
  --green:#2ec26b;
  --orange:#f99b3b;
  --red:#ef4343;
  --white:#fff;
}
*{box-sizing:border-box;margin:0;padding:0}
html,body{width:1200px;height:785px;overflow:hidden;background:var(--white);font-family:"Nunito Sans",sans-serif;color:var(--ink)}
.screen{position:absolute;width:1098px;height:686px;background:var(--purple);transform:scale(.5036);transform-origin:0 0;overflow:hidden}
.s1{left:31px;top:31px}.s2{left:615px;top:31px}.s3{left:31px;top:407px}.s4{left:615px;top:407px}
.brand{position:absolute;left:20px;top:10px;display:flex;align-items:center;gap:8px;color:var(--white);font-size:21px;font-weight:600}
.brand i{width:22px;height:22px;border-radius:50%;background:var(--white);display:block}
.nav a{position:absolute;top:6px;height:36px;line-height:36px;color:var(--white);font-size:11px;font-weight:600;text-decoration:none}
.nav .home{left:539px;width:54px;background:var(--cyan);text-align:center;border-radius:2px}
.nav svg{width:9px;height:9px;margin-left:4px;vertical-align:-1px}
.bell{position:absolute;left:945px;top:17px;width:14px;height:14px}
.bell-dot{position:absolute;left:957px;top:12px;width:5px;height:5px;border-radius:50%;background:var(--cyan)}
.user{position:absolute;left:988px;top:13px;display:flex;align-items:center;gap:7px;color:var(--white)}
.user .av{width:22px;height:22px;border-radius:50%;background:#b9b3c9}
.user b{display:block;font-size:10px;font-weight:600;line-height:11px}
.user small{display:block;font-size:8.5px;opacity:.75}
.user svg{width:9px;height:9px;margin-left:10px}
.side{position:absolute;left:6px;top:49px;width:195px}
.side .dash{height:36px;background:var(--cyan);color:var(--white);font-size:10.5px;font-weight:600;display:flex;align-items:center;padding:0 12px;gap:10px;border-radius:2px}
.side .dash .chev{margin-left:auto;width:10px;height:10px}
.side .ico{width:12px;height:12px}
.side ul{list-style:none;margin-top:3px}
.side li{height:30px;line-height:30px;margin-bottom:3.7px;padding-left:34px;font-size:10px;color:#ece6f8}
.side li.on{background:var(--white);color:var(--ink);border-radius:2px}
.side .cal{height:30px;display:flex;align-items:center;padding:0 12px;gap:10px;font-size:10.5px;color:var(--white)}
.side .cal .chev{margin-left:auto;width:10px;height:10px}
.card{position:absolute;left:208px;top:49px;width:884px;height:631px;background:var(--white);border-radius:6px}
.title{position:absolute;left:18px;top:20px;font-size:19px;font-weight:600}
.btn{position:absolute;top:18px;height:31px;border-radius:16px;font-size:10px;font-weight:600;display:flex;align-items:center;justify-content:center;gap:6px}
.btn svg{width:12px;height:12px}
.filters{border:1px solid var(--line);color:var(--purple-btn);width:76px}
.create{background:var(--purple-btn);color:var(--white);width:102px;left:764px}
.box{position:absolute;left:18px;top:67px;width:848px;border:1px solid var(--line);border-radius:3px;overflow:hidden}
.total{position:absolute;left:12px;top:12px;font-size:10.5px;color:var(--muted)}
.total b{color:var(--ink);margin-left:4px}
.legend-mini{position:absolute;right:12px;top:14px;font-size:8.5px;color:#8a8a98;display:flex;gap:16px}
.legend-mini span::before{content:"";display:inline-block;width:6px;height:6px;border-radius:50%;background:var(--c);margin-right:3px}
.legend-mini b{color:var(--ink);margin-left:3px}
.bar{position:absolute;left:12px;right:12px;top:33px;height:6px;border-radius:3px;display:flex;overflow:hidden}
.thead{position:absolute;left:0;top:54px;width:836px;border-top:1px solid var(--line);border-bottom:1px solid var(--line);font-size:9px;text-transform:uppercase;color:var(--ink)}
.tbody{position:absolute;left:0;width:836px;font-size:10px}
.row{display:grid;height:43.5px;align-items:center;border-bottom:1px solid var(--line)}
.row>div,.thead .h{padding-left:12px;white-space:nowrap;overflow:hidden}
.thead .h{display:flex;align-items:center;border-right:1px solid var(--line);height:100%}
.thead .h:last-child{border-right:0}
.h .arrow{width:9px;height:9px;margin-left:auto;margin-right:10px}
.dot::before{content:"";display:inline-block;width:6px;height:6px;border-radius:50%;background:var(--c);margin-right:7px;vertical-align:1px}
.person{display:flex;align-items:center;gap:6px}
.pav{width:17px;height:17px;border-radius:50%;background:var(--pc,#8d8597);flex:none}
.sc{width:17px;height:17px;border-radius:50%;background:#e4e4ea;font-size:7.5px;font-weight:700;display:flex;align-items:center;justify-content:center;flex:none}
.opts{display:flex;gap:14px;padding-left:16px!important}
.opts svg{width:12px;height:12px}
.scroll{position:absolute;right:6px;width:3px;border-radius:2px;background:#d9d9e2}
.g1{grid-template-columns:91px 122px 153px 158px 92px 152px 68px}
.g2{grid-template-columns:92px 183px 122px 183px 189px 67px}
.g4{grid-template-columns:184px 182px 201px 202px 67px}
.photo{width:64px;height:64px;border:2px solid var(--red);border-radius:3px;margin-left:56px;padding:2px}
.photo div{width:100%;height:100%;background:linear-gradient(160deg,#c9b49c,#6c5a4c)}
.chart-title{position:absolute;left:0;right:0;top:24px;text-align:center;font-size:10.5px;font-weight:600}
</style>
</head>
<body>
<svg width="0" height="0" style="position:absolute">
 <defs>
  <symbol id="pen" viewBox="0 0 16 16"><path d="M3 13l1-4 7-7 3 3-7 7-4 1zM10 3l3 3M2 15h12" fill="none" stroke="#6246ad" stroke-width="1.2"/></symbol>
  <symbol id="bin" viewBox="0 0 16 16"><path d="M3 4h10M6 4V2h4v2M4 4l1 10h6l1-10M7 7v5M9 7v5" fill="none" stroke="#ef4343" stroke-width="1.2"/></symbol>
  <symbol id="eye" viewBox="0 0 16 16"><path d="M1 8s3-5 7-5 7 5 7 5-3 5-7 5-7-5-7-5z" fill="none" stroke="#6246ad" stroke-width="1.2"/><circle cx="8" cy="8" r="2" fill="none" stroke="#6246ad" stroke-width="1.2"/></symbol>
  <symbol id="ok" viewBox="0 0 16 16"><circle cx="8" cy="8" r="6.5" fill="none" stroke="#1fa7d9" stroke-width="1.2"/><path d="M5 8l2 2 4-4" fill="none" stroke="#1fa7d9" stroke-width="1.2"/></symbol>
  <symbol id="no" viewBox="0 0 16 16"><circle cx="8" cy="8" r="6.5" fill="none" stroke="#ef4343" stroke-width="1.2"/><path d="M5.5 5.5l5 5M10.5 5.5l-5 5" fill="none" stroke="#ef4343" stroke-width="1.2"/></symbol>
  <symbol id="chev" viewBox="0 0 10 10"><path d="M2 3.5l3 3 3-3" fill="none" stroke="currentColor" stroke-width="1.3"/></symbol>
  <symbol id="chevr" viewBox="0 0 10 10"><path d="M3.5 2l3 3-3 3" fill="none" stroke="currentColor" stroke-width="1.3"/></symbol>
  <symbol id="down" viewBox="0 0 10 10"><path d="M5 1v8M2 6l3 3 3-3" fill="none" stroke="#6246ad" stroke-width="1.2"/></symbol>
  <symbol id="gauge" viewBox="0 0 12 12"><circle cx="6" cy="6" r="5" fill="none" stroke="#fff" stroke-width="1.2"/><path d="M6 6V3" stroke="#fff" stroke-width="1.2"/></symbol>
  <symbol id="calico" viewBox="0 0 12 12"><rect x="1" y="2" width="10" height="9" rx="1" fill="none" stroke="#fff" stroke-width="1"/><path d="M1 5h10M4 1v2M8 1v2" stroke="#fff"/></symbol>
  <symbol id="bellico" viewBox="0 0 14 14"><path d="M3 10V6a4 4 0 018 0v4l1 1H2zM6 12.5h2" fill="none" stroke="#fff" stroke-width="1.2"/></symbol>
  <symbol id="sliders" viewBox="0 0 12 12"><path d="M1 3h10M1 9h10" stroke="#6246ad"/><circle cx="4" cy="3" r="1.5" fill="#fff" stroke="#6246ad"/><circle cx="8" cy="9" r="1.5" fill="#fff" stroke="#6246ad"/></symbol>
  <symbol id="plus" viewBox="0 0 12 12"><circle cx="6" cy="6" r="5" fill="none" stroke="#fff"/><path d="M6 3.5v5M3.5 6h5" stroke="#fff"/></symbol>
 </defs>
</svg>

<!-- Screen 1: Managed Openings -->
<section class="screen s1">
 <div class="brand"><i></i>ShiftCover</div>
 <nav class="nav"><a class="home">Home</a><a style="left:612px">Demo Outbox</a><a style="left:711px">Location Admin<svg><use href="#chev"/></svg></a><a style="left:834px">Regular Staff<svg><use href="#chev"/></svg></a></nav>
 <svg class="bell"><use href="#bellico"/></svg><span class="bell-dot"></span>
 <div class="user"><span class="av" role="img" aria-label="User avatar"></span><div><b>John Doe</b><small>Manager</small></div><svg style="color:#fff"><use href="#chev"/></svg></div>
 <aside class="side">
  <div class="dash"><svg class="ico"><use href="#gauge"/></svg>Dashboard<svg class="chev" style="color:#fff"><use href="#chev"/></svg></div>
  <ul><li class="on">Managed Openings</li><li>Regular Staff Leave Requests</li><li>My Leave Requests</li><li>Location Overview</li><li>Pending Profile Images</li><li>Substitute Attendance</li></ul>
  <div class="cal"><svg class="ico"><use href="#calico"/></svg>Calendar<svg class="chev" style="color:#fff"><use href="#chevr"/></svg></div>
 </aside>
 <main class="card">
  <h1 class="title">Managed Openings</h1>
  <div class="btn filters" style="left:681px"><svg><use href="#sliders"/></svg>Filters</div>
  <div class="btn create"><svg><use href="#plus"/></svg>Create New</div>
  <div class="box" style="height:546px">
   <div class="total">Total:<b>20</b></div>
   <div class="legend-mini"><span style="--c:var(--blue)">Available:<b>19</b></span><span style="--c:var(--green)">Assigned:<b>1</b></span></div>
   <div class="bar"><span style="flex:19;background:var(--blue)"></span><span style="width:2px"></span><span style="flex:1.6;background:var(--green)"></span></div>
   <div class="thead row g1" style="height:35px"><div class="h">Status<svg class="arrow"><use href="#down"/></svg></div><div class="h">Category</div><div class="h">Regular Staff</div><div class="h">Summary</div><div class="h">Location</div><div class="h">Time Slots Summary</div><div class="h">Options</div></div>
   <div class="tbody" style="top:89px">
    <div class="row g1"><div class="dot" style="--c:var(--green)">Assigned</div><div>Food Service</div><div>Extra Duty</div><div>Immediate Need! Lorem Ipsu...</div><div>LJE</div><div>12/30 - 01/01 (2h 30m)</div><div class="opts"><svg><use href="#pen"/></svg><svg><use href="#bin"/></svg></div></div>
    <div class="row g1"><div class="dot" style="--c:var(--blue)">Available</div><div>Teacher</div><div class="person"><span class="pav" style="--pc:#8b5a4d" role="img" aria-label="Staff avatar"></span>Naomi Willis</div><div>Immediate Need! Dolor Amet</div><div>WDMS</div><div>02/12 - 02/16 (4h 10m)</div><div class="opts"><svg><use href="#pen"/></svg><svg><use href="#bin"/></svg></div></div>
    <div class="row g1"><div class="dot" style="--c:var(--blue)">Available</div><div>Bus Driver</div><div>Extra Duty</div><div>Immediate Need! Consectet...</div><div>WDMS</div><div>02/03 - 02/07 (4h 10m)</div><div class="opts"><svg><use href="#pen"/></svg><svg><use href="#bin"/></svg></div></div>
    <div class="row g1"><div class="dot" style="--c:var(--blue)">Available</div><div>Custodian</div><div>Extra Duty</div><div>Seeking Sub for Lorem Ipsum</div><div>FMS</div><div>01/06 - 01/10 (3h 50m)</div><div class="opts"><svg><use href="#pen"/></svg><svg><use href="#bin"/></svg></div></div>
    <div class="row g1"><div class="dot" style="--c:var(--blue)">Available</div><div>Teacher's Aide</div><div>Extra Duty</div><div>Seeking Sub for IT</div><div>FMS</div><div>01/20 - 01/23 (3h 20m)</div><div class="opts"><svg><use href="#pen"/></svg><svg><use href="#bin"/></svg></div></div>
    <div class="row g1"><div class="dot" style="--c:var(--blue)">Available</div><div>Food Service</div><div class="person"><span class="pav" style="--pc:#7a6150" role="img" aria-label="Staff avatar"></span>Gladys Richardson</div><div>Seeking Sub for SS</div><div>FMS</div><div>01/20 - 01/05 (3h 20m)</div><div class="opts"><svg><use href="#pen"/></svg><svg><use href="#bin"/></svg></div></div>
    <div class="row g1"><div class="dot" style="--c:var(--blue)">Available</div><div>Teacher's Aide</div><div class="person"><span class="pav" style="--pc:#6e7585" role="img" aria-label="Staff avatar"></span>Alan Bowman</div><div>Substitue Needed for Lorem...</div><div>LJE</div><div>01/20 - 01/05 (3h 20m)</div><div class="opts"><svg><use href="#pen"/></svg><svg><use href="#bin"/></svg></div></div>
    <div class="row g1"><div class="dot" style="--c:var(--blue)">Available</div><div>Bus Driver</div><div>Extra Duty</div><div>Immediate Need! Consectet...</div><div>WDMS</div><div>02/03 - 02/07 (4h 10m)</div><div class="opts"><svg><use href="#pen"/></svg><svg><use href="#bin"/></svg></div></div>
    <div class="row g1"><div class="dot" style="--c:var(--blue)">Available</div><div>Custodian</div><div>Extra Duty</div><div>Seeking Sub for Lorem Ipsum</div><div>FMS</div><div>01/06 - 01/10 (3h 50m)</div><div class="opts"><svg><use href="#pen"/></svg><svg><use href="#bin"/></svg></div></div>
    <div class="row g1"><div class="dot" style="--c:var(--blue)">Available</div><div>Teacher's Aide</div><div>Extra Duty</div><div>Seeking Sub for IT</div><div>FMS</div><div>01/20 - 01/23 (3h 20m)</div><div class="opts"><svg><use href="#pen"/></svg><svg><use href="#bin"/></svg></div></div>
    <div class="row g1"><div class="dot" style="--c:var(--blue)">Available</div><div>Food Service</div><div class="person"><span class="pav" style="--pc:#7a6150" role="img" aria-label="Staff avatar"></span>Gladys Richardson</div><div>Seeking Sub for SS</div><div>FMS</div><div>01/20 - 01/05 (3h 20m)</div><div class="opts"><svg><use href="#pen"/></svg><svg><use href="#bin"/></svg></div></div>
   </div>
   <div class="scroll" style="top:92px;height:240px"></div>
  </div>
 </main>
</section>

<!-- Screen 2: Regular Staff Leave Requests -->
<section class="screen s2">
 <div class="brand"><i></i>ShiftCover</div>
 <nav class="nav"><a class="home">Home</a><a style="left:612px">Demo Outbox</a><a style="left:711px">Location Admin<svg><use href="#chev"/></svg></a><a style="left:834px">Regular Staff<svg><use href="#chev"/></svg></a></nav>
 <svg class="bell"><use href="#bellico"/></svg><span class="bell-dot"></span>
 <div class="user"><span class="av" role="img" aria-label="User avatar"></span><div><b>John Doe</b><small>Manager</small></div><svg style="color:#fff"><use href="#chev"/></svg></div>
 <aside class="side">
  <div class="dash"><svg class="ico"><use href="#gauge"/></svg>Dashboard<svg class="chev" style="color:#fff"><use href="#chev"/></svg></div>
  <ul><li>Managed Openings</li><li class="on">Regular Staff Leave Requests</li><li>My Leave Requests</li><li>Location Overview</li><li>Pending Profile Images</li><li>Substitute Attendance</li></ul>
  <div class="cal"><svg class="ico"><use href="#calico"/></svg>Calendar<svg class="chev" style="color:#fff"><use href="#chevr"/></svg></div>
 </aside>
 <main class="card">
  <h1 class="title">Regular Staff Leave Requests</h1>
  <div class="btn filters" style="left:681px"><svg><use href="#sliders"/></svg>Filters</div>
  <div class="btn create"><svg><use href="#plus"/></svg>Create New</div>
  <div class="box" style="height:546px">
   <div class="total">Total:<b>20</b></div>
   <div class="legend-mini"><span style="--c:var(--orange)">Pending:<b>20</b></span></div>
   <div class="bar" style="background:var(--orange)"></div>
   <div class="thead" style="height:71px;display:grid;grid-template-columns:92px 183px 305px 189px 67px">
    <div class="h">Status<svg class="arrow"><use href="#down"/></svg></div><div class="h">Full Name</div>
    <div class="h" style="display:grid;grid-template-columns:122px 183px;grid-template-rows:35px 35px;padding:0">
     <div style="grid-column:1/3;text-align:center;align-self:center">Location</div>
     <div style="padding-left:12px;border-top:1px solid var(--line);border-right:1px solid var(--line);display:flex;align-items:center">Assignment</div>
     <div style="padding-left:12px;border-top:1px solid var(--line);display:flex;align-items:center">Prearranged Sub</div>
    </div>
    <div class="h">Time Slots Summary</div><div class="h">Options</div>
   </div>
   <div class="tbody" style="top:125px">
    <div class="row g2"><div class="dot" style="--c:var(--orange)">Pending</div><div class="person"><span class="pav" style="--pc:#6e7585" role="img" aria-label="Staff avatar"></span>Alan Bowman</div><div>N/A</div><div>N/A</div><div>12/22 - 12/22 (0h 30m)</div><div class="opts"><svg><use href="#pen"/></svg><svg><use href="#eye"/></svg></div></div>
    <div class="row g2"><div class="dot" style="--c:var(--orange)">Pending</div><div class="person"><span class="pav" style="--pc:#4a3a44" role="img" aria-label="Staff avatar"></span>Jeremy Gardner</div><div>N/A</div><div>N/A</div><div>12/24 - 12/30 (4h 45m)</div><div class="opts"><svg><use href="#pen"/></svg><svg><use href="#eye"/></svg></div></div>
    <div class="row g2"><div class="dot" style="--c:var(--orange)">Pending</div><div class="person"><span class="sc">SC</span>Scarlet Cook</div><div>Counselor</div><div></div><div>12/20 - 12/31 (4h 45m)</div><div class="opts"><svg><use href="#pen"/></svg><svg><use href="#eye"/></svg></div></div>
    <div class="row g2"><div class="dot" style="--c:var(--orange)">Pending</div><div class="person"><span class="pav" style="--pc:#a68b78" role="img" aria-label="Staff avatar"></span>Hannah Collins</div><div>N/A</div><div>N/A</div><div>12/20 - 01/09 (1h 45m)</div><div class="opts"><svg><use href="#pen"/></svg><svg><use href="#eye"/></svg></div></div>
    <div class="row g2"><div class="dot" style="--c:var(--orange)">Pending</div><div class="person"><span class="pav" style="--pc:#6b5a6e" role="img" aria-label="Staff avatar"></span>Monica Mason</div><div>Administrator</div><div class="person"><span class="pav" style="--pc:#7c7f88" role="img" aria-label="Staff avatar"></span>Ian Robertson</div><div>12/24 - 01/16 (5h 0m)</div><div class="opts"><svg><use href="#pen"/></svg><svg><use href="#eye"/></svg></div></div>
    <div class="row g2"><div class="dot" style="--c:var(--orange)">Pending</div><div class="person"><span class="pav" style="--pc:#55493f" role="img" aria-label="Staff avatar"></span>Gladys Herrera</div><div>Administrator</div><div></div><div>12/20 - 01/04 (2h 0m)</div><div class="opts"><svg><use href="#pen"/></svg><svg><use href="#eye"/></svg></div></div>
    <div class="row g2"><div class="dot" style="--c:var(--orange)">Pending</div><div class="person"><span class="pav" style="--pc:#6e7585" role="img" aria-label="Staff avatar"></span>Alan Bowman</div><div>N/A</div><div>N/A</div><div>12/22 - 12/22 (0h 30m)</div><div class="opts"><svg><use href="#pen"/></svg><svg><use href="#eye"/></svg></div></div>
    <div class="row g2"><div class="dot" style="--c:var(--orange)">Pending</div><div class="person"><span class="pav" style="--pc:#4a3a44" role="img" aria-label="Staff avatar"></span>Jeremy Gardner</div><div>N/A</div><div>N/A</div><div>12/24 - 12/30 (4h 45m)</div><div class="opts"><svg><use href="#pen"/></svg><svg><use href="#eye"/></svg></div></div>
    <div class="row g2"><div class="dot" style="--c:var(--orange)">Pending</div><div class="person"><span class="sc">SC</span>Scarlet Cook</div><div>Counselor</div><div></div><div>12/20 - 12/31 (4h 45m)</div><div class="opts"><svg><use href="#pen"/></svg><svg><use href="#eye"/></svg></div></div>
    <div class="row g2"><div class="dot" style="--c:var(--orange)">Pending</div><div class="person"><span class="pav" style="--pc:#a68b78" role="img" aria-label="Staff avatar"></span>Hannah Collins</div><div>N/A</div><div>N/A</div><div>12/20 - 01/09 (1h 45m)</div><div class="opts"><svg><use href="#pen"/></svg><svg><use href="#eye"/></svg></div></div>
   </div>
   <div class="scroll" style="top:128px;height:240px"></div>
  </div>
 </main>
</section>

<!-- Screen 3: Location Overview -->
<section class="screen s3">
 <div class="brand"><i></i>ShiftCover</div>
 <nav class="nav"><a class="home">Home</a><a style="left:612px">Demo Outbox</a><a style="left:711px">Location Admin<svg><use href="#chev"/></svg></a><a style="left:834px">Regular Staff<svg><use href="#chev"/></svg></a></nav>
 <svg class="bell"><use href="#bellico"/></svg><span class="bell-dot"></span>
 <div class="user"><span class="av" role="img" aria-label="User avatar"></span><div><b>John Doe</b><small>Manager</small></div><svg style="color:#fff"><use href="#chev"/></svg></div>
 <aside class="side">
  <div class="dash"><svg class="ico"><use href="#gauge"/></svg>Dashboard<svg class="chev" style="color:#fff"><use href="#chev"/></svg></div>
  <ul><li>Managed Openings</li><li>Regular Staff Leave Requests</li><li>My Leave Requests</li><li class="on">Location Overview</li><li>Pending Profile Images</li><li>Substitute Attendance</li></ul>
  <div class="cal"><svg class="ico"><use href="#calico"/></svg>Calendar<svg class="chev" style="color:#fff"><use href="#chevr"/></svg></div>
 </aside>
 <main class="card">
  <h1 class="title">Location Overview</h1>
  <div class="btn filters" style="left:789px"><svg><use href="#sliders"/></svg>Filters</div>
  <div class="box" style="height:446px">
   <div class="chart-title">Leave Request / Openings / Assignments</div>
   <svg width="848" height="446" style="position:absolute;left:0;top:0" font-family="Nunito Sans, sans-serif" font-size="9" fill="#6b6b78">
    <g stroke="#ececf2">
     <line x1="54" x2="819" y1="62" y2="62"/><line x1="54" x2="819" y1="123" y2="123"/><line x1="54" x2="819" y1="184" y2="184"/><line x1="54" x2="819" y1="245" y2="245"/><line x1="54" x2="819" y1="306" y2="306"/><line x1="54" x2="819" y1="367" y2="367"/>
    </g>
    <g text-anchor="end"><text x="45" y="65">10</text><text x="45" y="126">8</text><text x="45" y="187">6</text><text x="45" y="248">4</text><text x="45" y="309">2</text><text x="45" y="370">0</text></g>
    <rect x="127" y="275" width="49" height="92" fill="#18a9f5"/>
    <rect x="127" y="245" width="49" height="30" fill="#2ec26b"/>
    <rect x="182" y="245" width="49" height="122" fill="#f99b3b"/>
    <rect x="382" y="214" width="49" height="153" fill="#18a9f5"/>
    <rect x="437" y="245" width="49" height="122" fill="#f99b3b"/>
    <rect x="638" y="184" width="49" height="183" fill="#18a9f5"/>
    <rect x="693" y="62" width="49" height="305" fill="#f99b3b"/>
    <g text-anchor="middle"><text x="179" y="382">Lake Jonas Elementary</text><text x="434" y="382">Feestberg Middle School</text><text x="690" y="382">West Devante Middle School</text></g>
    <line x1="0" x2="848" y1="408" y2="408" stroke="#e7e7ef"/>
    <g font-size="10" fill="#2b2b3a">
     <rect x="228" y="422" width="12" height="12" fill="#18a9f5"/><text x="248" y="431">Openings - Unfilled</text>
     <rect x="360" y="422" width="12" height="12" fill="#2ec26b"/><text x="380" y="431">Openings - Filled</text>
     <rect x="481" y="422" width="12" height="12" fill="#f99b3b"/><text x="501" y="431">Leave Requests - Pending</text>
    </g>
   </svg>
  </div>
 </main>
</section>

<!-- Screen 4: Pending Profile Images -->
<section class="screen s4">
 <div class="brand"><i></i>ShiftCover</div>
 <nav class="nav"><a class="home">Home</a><a style="left:612px">Demo Outbox</a><a style="left:711px">Location Admin<svg><use href="#chev"/></svg></a><a style="left:834px">Regular Staff<svg><use href="#chev"/></svg></a></nav>
 <svg class="bell"><use href="#bellico"/></svg><span class="bell-dot"></span>
 <div class="user"><span class="av" role="img" aria-label="User avatar"></span><div><b>John Doe</b><small>Manager</small></div><svg style="color:#fff"><use href="#chev"/></svg></div>
 <aside class="side">
  <div class="dash"><svg class="ico"><use href="#gauge"/></svg>Dashboard<svg class="chev" style="color:#fff"><use href="#chev"/></svg></div>
  <ul><li>Managed Openings</li><li>Regular Staff Leave Requests</li><li>My Leave Requests</li><li>Location Overview</li><li class="on">Pending Profile Images</li><li>Substitute Attendance</li></ul>
  <div class="cal"><svg class="ico"><use href="#calico"/></svg>Calendar<svg class="chev" style="color:#fff"><use href="#chevr"/></svg></div>
 </aside>
 <main class="card">
  <h1 class="title">Pending Profile Images</h1>
  <div class="btn filters" style="left:789px"><svg><use href="#sliders"/></svg>Filters</div>
  <div class="box" style="height:546px">
   <div class="total">Total:<b>20</b></div>
   <div class="legend-mini"><span style="--c:var(--red)">Unverified:<b>9</b></span></div>
   <div class="bar" style="background:var(--red)"></div>
   <div class="thead" style="height:71px;display:grid;grid-template-columns:184px 182px 403px 67px">
    <div class="h">Last Name<svg class="arrow"><use href="#down"/></svg></div><div class="h">First Name</div>
    <div class="h" style="display:grid;grid-template-columns:201px 202px;grid-template-rows:35px 35px;padding:0">
     <div style="grid-column:1/3;text-align:center;align-self:center">Profile Images</div>
     <div style="border-top:1px solid var(--line);border-right:1px solid var(--line);display:flex;align-items:center;justify-content:center">Pending</div>
     <div style="border-top:1px solid var(--line);display:flex;align-items:center;justify-content:center">Previously Verified</div>
    </div>
    <div class="h">Options</div>
   </div>
   <div class="tbody" style="top:125px">
    <div class="row g4" style="height:86px"><div>Morales</div><div>June</div><div><div class="photo"><div role="img" aria-label="Pending profile photo"></div></div></div><div style="text-align:center;padding:0">N/A</div><div class="opts"><svg><use href="#ok"/></svg><svg><use href="#no"/></svg></div></div>
    <div class="row g4" style="height:86px"><div>Stephens</div><div>Priscilia</div><div><div class="photo"><div role="img" aria-label="Pending profile photo"></div></div></div><div style="text-align:center;padding:0">N/A</div><div class="opts"><svg><use href="#ok"/></svg><svg><use href="#no"/></svg></div></div>
    <div class="row g4" style="height:86px"><div>Stevens</div><div>Mason</div><div><div class="photo"><div role="img" aria-label="Pending profile photo"></div></div></div><div style="text-align:center;padding:0">N/A</div><div class="opts"><svg><use href="#ok"/></svg><svg><use href="#no"/></svg></div></div>
    <div class="row g4" style="height:86px"><div>Walters</div><div>Kim</div><div><div class="photo"><div role="img" aria-label="Pending profile photo"></div></div></div><div style="text-align:center;padding:0">N/A</div><div class="opts"><svg><use href="#ok"/></svg><svg><use href="#no"/></svg></div></div>
    <div class="row g4" style="height:86px"><div>Wills</div><div>Naomi</div><div><div class="photo"><div role="img" aria-label="Pending profile photo"></div></div></div><div style="text-align:center;padding:0">N/A</div><div class="opts"><svg><use href="#ok"/></svg><svg><use href="#no"/></svg></div></div>
   </div>
   <div class="scroll" style="top:128px;height:240px"></div>
  </div>
 </main>
</section>
</body>
</html>
```